Satin Decor Paint Label

We will have three different sizes for this label but the dimensions for the medium size are 2" tall by 11.75'' wide. Please work off that.

Our colors are typically black and white but feel free to incorporate silver, gold, bronze or any combination. We would like to see multiple color variations of your designs.

General Info needed on label:
2736
Coatings
Interior Decor Paint
Furniture, Trim, Cabinets
Acrylic Waterborne Urethane
Satin Finish
16 FL. OZ. - 473 mL
````````````````````````````````````````````````````````````````````````````````````````````
Your design does not have to be the same as the one in the attached image.

You can put Satin Finish or Interior Decor Paint or something else going vertically up the side.

The label will be on a container like the the one in the attached image. Please have your design work on the same container.

```html
<!DOCTYPE html>
<html lang="en">
<head>
<meta charset="utf-8">
<title>2736 Coatings – Satin Finish Label</title>
<link rel="stylesheet" href="https://fonts.googleapis.com/css2?family=Poppins:wght@500;600&display=swap">
<style>
  :root {
    --page: #d2d2d2;
    --label-black: #141414;
    --white: #ffffff;
    --rule: #8a8a8a;
    --ink: #161616;
  }
  * { margin: 0; padding: 0; box-sizing: border-box; }
  html, body {
    width: 1200px; height: 1200px; overflow: hidden;
    background: var(--page);
  }
  .label {
    position: absolute; left: 50px; top: 312px;
    width: 1100px; height: 575px;
    background: var(--label-black);
    color: var(--white);
    font-family: "Poppins", sans-serif;
  }
  .side-stripe {
    position: absolute; left: 167px; top: 0;
    width: 80px; height: 100%;
    background: var(--white);
    display: flex; align-items: center; justify-content: center;
  }
  .side-stripe span {
    transform: rotate(-90deg);
    white-space: nowrap;
    color: var(--ink);
    font-weight: 600; font-size: 54px; letter-spacing: 1px;
  }
  .brand-name {
    position: absolute; left: 247px; top: 150px; width: 626px;
    text-align: center;
    font-weight: 600; font-size: 62px; letter-spacing: 4px; line-height: 1;
    color: var(--white);
  }
  .product-type {
    position: absolute; left: 247px; top: 296px; width: 626px;
    text-align: center;
    font-weight: 500; font-size: 31px; letter-spacing: 6px;
  }
  .rule {
    position: absolute; left: 260px; width: 590px; height: 2px;
    background: var(--rule);
  }
  .rule.top { top: 354px; }
  .rule.bottom { top: 412px; }
  .uses {
    position: absolute; left: 278px; top: 362px;
    width: 570px; height: 46px;
    display: flex; align-items: center; justify-content: space-between;
    font-weight: 500; font-size: 30px;
  }
  .use { display: flex; align-items: center; gap: 10px; }
  .use svg { width: 22px; height: 24px; }
  .formula {
    position: absolute; left: 247px; top: 468px; width: 626px;
    text-align: center; font-weight: 500; font-size: 21px; letter-spacing: 4px;
  }
  .volume {
    position: absolute; left: 247px; top: 503px; width: 626px;
    text-align: center; font-weight: 500; font-size: 22px;
  }
</style>
</head>
<body>
  <div class="label">
    <div class="side-stripe"><span>SATIN FINISH</span></div>

    <div class="brand-name">2736 COATINGS</div>

    <div class="product-type">INTERIOR DECOR PAINT</div>

    <div class="rule top"></div>
    <div class="uses">
      <div class="use">
        <svg viewBox="0 0 22 24" fill="none" stroke="#fff" stroke-width="1.6">
          <rect x="2" y="2" width="10" height="18"/><rect x="12" y="10" width="8" height="10"/>
          <line x1="3" y1="20" x2="3" y2="23"/><line x1="19" y1="20" x2="19" y2="23"/>
        </svg>Furniture
      </div>
      <div class="use">
        <svg viewBox="0 0 22 24" fill="none" stroke="#fff" stroke-width="1.6">
          <rect x="8" y="2" width="12" height="12"/><rect x="5" y="6" width="12" height="12"/><rect x="2" y="10" width="12" height="12"/>
        </svg>Trim
      </div>
      <div class="use">
        <svg viewBox="0 0 22 24" fill="none" stroke="#fff" stroke-width="1.6">
          <rect x="3" y="2" width="16" height="20"/><line x1="3" y1="9" x2="19" y2="9"/><line x1="3" y1="15" x2="19" y2="15"/>
          <line x1="9" y1="5.5" x2="13" y2="5.5"/><line x1="9" y1="12" x2="13" y2="12"/><line x1="9" y1="18.5" x2="13" y2="18.5"/>
        </svg>Cabinets
      </div>
    </div>
    <div class="rule bottom"></div>

    <div class="formula">ACRYLIC WATERBORNE URETHANE</div>
    <div class="volume">16 FL. OZ. - 473 mL</div>
  </div>
</body>
</html>
```